Book cover for my book "Amber Orchard Letters"

Simple graphic with the title "Amber Orchard Letters" for a book I am self publishing. This book teaches people how to divorce with kindness and compassion without compromising their legal rights and getting what is fair. I am a lawyer telling them everything on how to hire a lawyer, what process to choose, how to build a support system, how to keep the kids out of it. It should exude authority, but also kindness and compassion. It's real legal information but from a lens that doesn't give a bunch of money to lawyers to burn down your family.

Target Market(s)

People seeking to divorce but don't want to spend a bunch of money or destroy their spouse

Industry/Entity Type

Legal

Requirements
Must have
• Dignity
Nice to have
• Envision two people parting, moving away from each other but something that is altruistic popping up between them? I'm not artist. Keep in mind "couple" is generic so not gender specific.
Should not have
• Trite things like a handshake,

```html
<!DOCTYPE html>
<html lang="en">
<head>
<meta charset="utf-8">
<title>Amber Orchard Letters — Book Cover Wrap</title>
<link rel="stylesheet" href="https://fonts.googleapis.com/css2?family=Cinzel:wght@400;600&family=Libre+Baskerville:wght@400;700&display=swap">
<style>
  :root {
    --stage: #e8e8ea;
    --paper: #ffffff;
    --maroon: #8a2433;
    --ink: #2b2b2b;
    --muted: #555555;
    --spine: #5b5f58;
    --spine-text: #f1efe9;
    --photo-light: #c4c6ca;
    --photo-mid: #8d929a;
    --photo-dark: #5a5f68;
  }
  * { margin: 0; padding: 0; box-sizing: border-box; }
  html, body { width: 1200px; height: 2164px; overflow: hidden; }
  body {
    background: var(--stage);
    display: flex; align-items: center; justify-content: center;
    font-family: "Libre Baskerville", Georgia, serif;
    color: var(--ink);
  }
  .cover-wrap {
    display: flex;
    width: 1104px; height: 780px;
    box-shadow: 0 6px 24px rgba(0,0,0,0.18);
  }
  .brand {
    display: flex; align-items: center; gap: 8px;
    font-family: "Libre Baskerville", Georgia, serif;
    font-size: 11px; letter-spacing: 2px;
    color: var(--maroon); font-weight: 400;
    text-transform: uppercase;
  }
  .brand-dot { width: 14px; height: 14px; border-radius: 50%; background: var(--maroon); }

  /* Back cover */
  .back-cover {
    width: 520px; background: var(--paper);
    padding: 44px 46px; position: relative;
  }
  .back-cover .brand { margin-bottom: 40px; }
  .back-heading {
    font-size: 14px; font-weight: 700; margin-bottom: 10px; color: var(--ink);
  }
  .back-copy {
    font-size: 10.5px; line-height: 1.75; color: var(--muted);
    margin-bottom: 28px; text-align: justify;
  }
  .author-back {
    position: absolute; left: 46px; bottom: 56px;
    font-size: 11px; letter-spacing: 2px; color: var(--ink);
  }

  /* Spine */
  .spine {
    width: 64px; background: var(--spine);
    display: flex; flex-direction: column; align-items: center;
    padding: 36px 0;
  }
  .spine-title {
    writing-mode: vertical-rl;
    font-family: "Cinzel", "Times New Roman", serif;
    font-weight: 400;
    font-size: 22px; letter-spacing: 4px; color: var(--spine-text);
    text-transform: uppercase; margin-top: 20px;
  }

  /* Front cover */
  .front-cover {
    width: 520px; background: var(--paper);
    position: relative; display: flex; flex-direction: column; align-items: center;
  }
  .front-cover .brand { position: absolute; top: 26px; z-index: 2; }
  .cover-photo {
    width: 100%; height: 500px;
    background: linear-gradient(180deg,
      #ffffff 0%,
      var(--photo-light) 12%,
      var(--photo-mid) 30%,
      var(--photo-dark) 55%,
      var(--photo-mid) 78%,
      #ffffff 100%);
  }
  .front-title {
    font-family: "Cinzel", "Times New Roman", serif;
    font-weight: 400; color: var(--maroon);
    font-size: 46px; line-height: 1.1; text-align: center;
    text-transform: uppercase; margin-top: 34px; letter-spacing: 1px;
  }
  .author-front {
    margin-top: 18px; font-size: 11px; letter-spacing: 3px; color: var(--muted);
  }
</style>
</head>
<body>
  <main class="cover-wrap">
    <section class="back-cover">
      <div class="brand"><span class="brand-dot"></span>The Gentle Counsel</div>
      <h2 class="back-heading">What is lorem ipsum text?</h2>
      <p class="back-copy">A lawyer's guide to ending a marriage with care. Learn how to hire the right counsel, choose a process that fits your family, and protect what is fair without burning down the home you built. Each chapter offers clear legal steps, honest costs, and gentle advice for building a support system that carries you through the hardest months.</p>
      <h2 class="back-heading">Why do we use it?</h2>
      <p class="back-copy">Because divorce does not have to be a war. Children deserve to stay out of the conflict, and both partners deserve dignity. This book shows how kindness and firm legal rights can stand side by side, so you can close one chapter and open the next with your peace intact.</p>
      <p class="author-back">AUTHOR NAME</p>
    </section>

    <section class="spine">
      <h2 class="spine-title">Amber Orchard Letters</h2>
    </section>

    <section class="front-cover">
      <div class="brand"><span class="brand-dot"></span>The Gentle Counsel</div>
      <div class="cover-photo" role="img" aria-label="Photograph of a couple sitting apart in quiet reflection under a soft cloudy sky, fading into white"></div>
      <h1 class="front-title">Amber Orchard<br>Letters</h1>
      <p class="author-front">AUTHOR NAME</p>
    </section>
  </main>
</body>
</html>
```